ONLINE MATTRESS COMPANY REQUIRING BOX DESIGN FOR MATTRESS IN A BOX

WE NEED A BOX DESIGN FOR A NEW COMPANY THAT SELLS A MATTRESS IN A BOX (SIMILAR TO VELNOR.COM) THAT INCORPORATES ONLY 2 COLOURS (TEAL & BLACK) THE BASE COLOUR OF BOX IS WHITE. THE DESIGN HAS TO INSPIRE MILLENNIAL AND YOUNG SHOPPERS TO WANT TO PURCHASE THE PRODUCT. BOX SHOULD BE SIMPLE AND CLEAN. ONE SIDE HAS TO SHOW THE OPENING INSTRUCTIONS WHICH ARE ATTACHED IN A SAMPLE BOX.

Target Market(s)

MILLENNIALS

Industry/Entity Type

Furniture Store

Font styles to use
Serif
Sans Serif

Colors
ffffff
33b8a4

Requirements
Must have
• ONE SIDE MUST HAVE OPEN INSTRUCTIONS (SEE EXAMPLE); THE FACTORY CAN ONLY PRING ON A WHITE BOX WITH 2 COLOURS. THE WRITING AND SHAPES CAN BE TEAL AND BLACK BUT THE WHOLE BOX CANNOT BE TEAL AND BLACK, JUST THE ART WORK.
Should not have
• CAN ONLY BE 2 COLOURS; BOX COLOUR IS WHITE ; TEAL & BLACK AS OTHER INK COLOURS.

SHOULD NOT SHOW LOGO VERTICALLY (UP AND DOWN) BECAUSE IT IS HARD TO READ, SHOULD BE HORIZONTAL.

DO NOT SHOW MATTRESS OR PILLOW ON BOX IT'S ONLY TO HELP GUIDE YOU SO KNOW WHAT THE PRODUCT IS!

```html
<!DOCTYPE html>
<html lang="en">
<head>
<meta charset="utf-8">
<title>Sovela Mattress Box Artwork</title>
<link rel="stylesheet" href="https://fonts.googleapis.com/css2?family=Jost:wght@400;600&family=Lato:wght@300;400;700&display=swap">
<style>
  :root {
    --teal: #2fa596;
    --teal-dark: #248a7d;
    --black: #0b0b0b;
    --white: #ffffff;
    --stage: #e9e9e9;
    --edge: #d2d2d2;
  }
  * { box-sizing: border-box; margin: 0; padding: 0; }
  html, body { width: 1139px; height: 1200px; overflow: hidden; }
  body {
    background: var(--stage);
    font-family: "Lato", sans-serif;
    position: relative;
  }
  .dieline {
    position: absolute;
    left: 30px; top: 230px;
    display: flex;
    gap: 10px;
  }
  .panel {
    position: relative;
    width: 262px; height: 740px;
    background: var(--white);
    border: 1px solid var(--edge);
    overflow: hidden;
  }
  .band {
    position: absolute;
    left: 0; right: 0; top: 150px; height: 128px;
    background: var(--black);
  }
  .brand {
    position: absolute;
    left: 18px; top: 34px;
    font-family: "Jost", sans-serif;
    font-weight: 400;
    font-size: 46px;
    letter-spacing: 1px;
    color: var(--teal);
    line-height: 1;
  }
  .panel--back .brand { left: 0; right: 0; text-align: center; }
  .band-pattern { position: absolute; right: 0; top: 0; width: 110px; height: 128px; }
  .product-name {
    position: absolute; left: 18px; top: 296px;
    font-family: "Jost", sans-serif; font-weight: 600;
    font-size: 13px; letter-spacing: .3px; color: var(--black);
  }
  .size-tag {
    position: absolute; right: 0; top: 278px;
    width: 96px; height: 38px;
    background: var(--teal);
    clip-path: polygon(0 0, 100% 0, 100% 100%, 18% 100%);
    color: var(--white);
    font-family: "Jost", sans-serif; font-weight: 600; font-size: 14px;
    display: flex; align-items: center; justify-content: flex-end; padding-right: 12px;
  }
  .tagline {
    position: absolute; left: 0; right: 0; top: 440px;
    text-align: center;
    font-weight: 300; font-size: 36px; line-height: 1.05;
    color: var(--teal); letter-spacing: 1px;
  }
  .handling {
    position: absolute; left: 24px; bottom: 22px;
    display: flex; gap: 12px; align-items: flex-end;
  }
  .instructions { position: absolute; left: 0; right: 0; top: 310px; }
  .instructions h2 {
    text-align: center; font-family: "Jost", sans-serif; font-weight: 600;
    font-size: 13px; color: var(--teal); letter-spacing: .3px; margin-bottom: 14px;
  }
  .steps { list-style: none; padding: 0 22px 0 30px; }
  .step { display: flex; align-items: center; gap: 10px; height: 74px; }
  .step-icon { flex: 0 0 auto; }
  .step p { font-size: 8.5px; font-weight: 700; color: var(--teal); line-height: 1.25; }
</style>
</head>
<body>
<main class="dieline">

  <section class="panel panel--front">
    <div class="band">
      <span class="brand">Sovela</span>
      <svg class="band-pattern" viewBox="0 0 110 128" role="img" aria-label="Teal mattress-spring lattice pattern">
        <polygon points="0,0 110,0 110,128 55,128" fill="var(--teal-dark)"/>
      </svg>
    </div>
    <p class="product-name">ORIGINAL MATTRESS</p>
    <div class="size-tag">CAL King</div>
    <p class="tagline">SLEEP<br>MADE<br>SIMPLE</p>
    <div class="handling">
      <svg width="30" height="30" viewBox="0 0 30 30" aria-label="This way up">
        <g fill="var(--black)">
          <polygon points="8,2 3,10 13,10"/><rect x="6.5" y="9" width="3" height="12"/>
          <polygon points="22,2 17,10 27,10"/><rect x="20.5" y="9" width="3" height="12"/>
          <rect x="2" y="25" width="26" height="3"/>
        </g>
      </svg>
      <svg width="28" height="28" viewBox="0 0 28 28" aria-label="Recyclable">
        <circle cx="14" cy="14" r="12" fill="none" stroke="var(--black)" stroke-width="3"/>
      </svg>
    </div>
  </section>

  <section class="panel panel--side">
    <div class="band"><span class="brand">Sovela</span></div>
    <p class="product-name">ORIGINAL MATTRESS</p>
    <div class="size-tag">CAL King</div>
    <p class="tagline">SLEEP<br>MADE<br>SIMPLE</p>
  </section>

  <section class="panel panel--back">
    <div class="band"><span class="brand">Sovela</span></div>
    <div class="instructions">
      <h2>SETUP INSTRUCTIONS</h2>
      <ol class="steps">
        <li class="step">
          <svg class="step-icon" width="58" height="52" viewBox="0 0 58 52"><circle cx="33" cy="26" r="22" fill="none" stroke="var(--teal)" stroke-width="2"/><circle cx="33" cy="26" r="12" fill="var(--teal)" opacity=".35" role="img" aria-label="Icon: box opened and laid on its side"/><circle cx="10" cy="26" r="9" fill="var(--teal)"/><text x="10" y="30" text-anchor="middle" font-size="11" font-weight="700" fill="#fff" font-family="Lato, sans-serif">1</text></svg>
          <p>Open the box from the top and lay it on its side to pull out the mattress.</p>
        </li>
        <li class="step">
          <svg class="step-icon" width="58" height="52" viewBox="0 0 58 52"><circle cx="33" cy="26" r="22" fill="none" stroke="var(--teal)" stroke-width="2"/><circle cx="33" cy="26" r="12" fill="var(--teal)" opacity=".35" role="img" aria-label="Icon: mattress unrolling"/><circle cx="10" cy="26" r="9" fill="var(--teal)"/><text x="10" y="30" text-anchor="middle" font-size="11" font-weight="700" fill="#fff" font-family="Lato, sans-serif">2</text></svg>
          <p>Allow the mattress to unfold and straighten flat.</p>
        </li>
        <li class="step">
          <svg class="step-icon" width="58" height="52" viewBox="0 0 58 52"><circle cx="33" cy="26" r="22" fill="none" stroke="var(--teal)" stroke-width="2"/><circle cx="33" cy="26" r="12" fill="var(--teal)" opacity=".35" role="img" aria-label="Icon: mattress expanding with timer"/><circle cx="10" cy="26" r="9" fill="var(--teal)"/><text x="10" y="30" text-anchor="middle" font-size="11" font-weight="700" fill="#fff" font-family="Lato, sans-serif">3</text></svg>
          <p>You can use the mattress 2-4 hours after opening but may need 24-48 hours for optimum expansion and comfort.</p>
        </li>
        <li class="step">
          <svg class="step-icon" width="58" height="52" viewBox="0 0 58 52"><circle cx="33" cy="26" r="22" fill="none" stroke="var(--teal)" stroke-width="2"/><circle cx="33" cy="26" r="12" fill="var(--teal)" opacity=".35" role="img" aria-label="Icon: recycling"/><circle cx="10" cy="26" r="9" fill="var(--teal)"/><text x="10" y="30" text-anchor="middle" font-size="11" font-weight="700" fill="#fff" font-family="Lato, sans-serif">4</text></svg>
          <p>Recycle the box and do your little bit for the planet.</p>
        </li>
        <li class="step">
          <svg class="step-icon" width="58" height="52" viewBox="0 0 58 52"><circle cx="33" cy="26" r="22" fill="none" stroke="var(--teal)" stroke-width="2"/><circle cx="33" cy="26" r="12" fill="var(--teal)" opacity=".35" role="img" aria-label="Icon: resting on the mattress"/><circle cx="10" cy="26" r="9" fill="var(--teal)"/><text x="10" y="30" text-anchor="middle" font-size="11" font-weight="700" fill="#fff" font-family="Lato, sans-serif">5</text></svg>
          <p>Now it's time to relax and get a great night's sleep.</p>
        </li>
      </ol>
    </div>
  </section>

  <section class="panel panel--side">
    <div class="band">
      <span class="brand">Sovela</span>
      <svg class="band-pattern" viewBox="0 0 110 128" role="img" aria-label="Teal mattress-spring lattice pattern">
        <polygon points="0,0 110,0 110,128 55,128" fill="var(--teal-dark)"/>
      </svg>
    </div>
    <p class="product-name">ORIGINAL MATTRESS</p>
    <div class="size-tag">CAL King</div>
    <p class="tagline">SLEEP<br>MADE<br>SIMPLE</p>
  </section>

</main>
</body>
</html>
```